Business card design needed

I need a business card design for a new online retail business based in Australia. I am unsure of the exact content of what I will be selling but it will be probably women's clothing, accessories, gym wear, gifts and maybe homeware linen. I am wanting a classy design that portrays the image of class/style/upmarket.

Target Market(s)

predominantely women - 20-50 age group

Industry/Entity Type

Retail

Contact Information for Business Card

Purely Lustre
Karen Whitlow
Director
ABN 73215548906
17 Harcourt Lane Dunmore Ridge NSW 2291
ph: +61 427 390 845
sales@purelylustre.com.au

Logo Text

I am open for suggestions here

Requirements
Must have
• The design must be both sides of the card

```html
<!DOCTYPE html>
<html lang="en">
<head>
<meta charset="utf-8">
<title>Purely Lustre – Business Card</title>
<link href="https://fonts.googleapis.com/css2?family=Poiret+One&family=Cormorant+Garamond:ital,wght@1,500&display=swap" rel="stylesheet">
<style>
  :root {
    --card-grey: #6d6e71;
    --blush: #f2c4d6;
    --white: #ffffff;
    --paper: #ffffff;
  }
  html, body {
    margin: 0;
    padding: 0;
    width: 1200px;
    height: 333px;
    overflow: hidden;
    background: var(--paper);
  }
  .sheet {
    position: relative;
    width: 1200px;
    height: 333px;
  }
  .card {
    position: absolute;
    top: 0;
    height: 333px;
    background: var(--card-grey);
    overflow: hidden;
    font-family: "Poiret One", sans-serif;
  }
  .card--front { left: 0; width: 577px; }
  .card--back { left: 622px; width: 578px; }

  .front-ornament {
    position: absolute;
    left: 204px;
    top: 22px;
    width: 160px;
    height: 163px;
    border-radius: 45% 45% 50% 50%;
    background: radial-gradient(ellipse at center, rgba(242,196,214,0.9) 0%, rgba(242,196,214,0.45) 55%, rgba(242,196,214,0) 75%);
  }
  .brand-name {
    position: absolute;
    left: 0;
    width: 577px;
    top: 182px;
    margin: 0;
    text-align: center;
    color: var(--white);
    font-weight: 400;
    font-size: 50px;
    letter-spacing: 1px;
    line-height: 1;
  }
  .brand-tagline {
    position: absolute;
    left: 0;
    width: 577px;
    top: 243px;
    margin: 0;
    text-align: center;
    color: var(--blush);
    font-family: "Cormorant Garamond", serif;
    font-style: italic;
    font-weight: 500;
    font-size: 19px;
    letter-spacing: 0.5px;
  }

  .back-ornament {
    position: absolute;
    left: 312px;
    top: 0;
    width: 266px;
    height: 333px;
    background: radial-gradient(ellipse 60% 55% at 60% 45%, rgba(255,255,255,0.85) 0%, rgba(255,255,255,0.4) 55%, rgba(255,255,255,0) 80%);
  }
  .contact {
    position: absolute;
    left: 40px;
    top: 139px;
    color: var(--white);
  }
  .contact p { margin: 0; line-height: 1; }
  .contact__name { font-size: 21px; margin-bottom: 9px !important; }
  .contact__abn { font-size: 15px; color: var(--blush); margin-bottom: 6px !important; }
  .contact__address { font-size: 13px; line-height: 15px !important; margin-bottom: 5px !important; }
  .contact__phone { font-size: 15px; color: var(--blush); margin-bottom: 6px !important; }
  .contact__email { font-size: 18px; }
</style>
</head>
<body>
<main class="sheet">
  <section class="card card--front">
    <div class="front-ornament" role="img" aria-label="Blush pink damask ornament"></div>
    <h1 class="brand-name">Purely Lustre</h1>
    <p class="brand-tagline">womans apparel</p>
  </section>

  <section class="card card--back">
    <div class="contact">
      <p class="contact__name">Karen Whitlow/Director</p>
      <p class="contact__abn">ABN 73215548906</p>
      <p class="contact__address">17 Harcourt Lane<br>Dunmore Ridge<br>NSW 2291</p>
      <p class="contact__phone">ph: +61 427 390 845</p>
      <p class="contact__email">sales@purelylustre.com.au</p>
    </div>
    <div class="back-ornament" role="img" aria-label="Large white damask ornament"></div>
  </section>
</main>
</body>
</html>
```